Plakat-Design für Herbstausstellung
Zielgruppe
Wir sind im Motorradhandel, inkl. Motorrad Bekleidung/Zubehör, tätig. Für unsere Herbstausstellung brauchen wir ein neues Plakat-Design. Unsere Zielgruppe sind im allgemeinen Männer und Frauen im Alter von 18-65 Jahre.
Aufgabenstellung
Das Plakat sollte Hochformat sein.
Angaben welche ersichtlich sein sollten: Unser Logo (Velo Kranz);Herbst-Ausstellung; Datum der Herbstausstellung (20.-22.10.17); Öffnungszeiten (Fr. 14-19h/Sa. 8-19h/So. 9-16h); Saisonausverkauf mit -20% auf Motorradbekleidung und Zubehör (nur auf nicht reduzierte Lagerware); Unsere Livemusik im Festzelt ( Freitag ab 20.00 Uhr Vinyl Abend mit Dustrider, Samstag ab 20.00 Uhr Festmusik mit Bergklang-Ost, Sonntag Matinée 09.00-16.00 Uhr), www.velo-kranz.ch)<- kann klein dargestellt werden; Unsere Markenvertretungen (QRZ, FVL, Harimo)
Vom Design her ist der Kreativität keine Grenze gesetzt (In den Dateianhängen ist unser altes Plakat-Design beigefügt, als Anhaltspunkt für den Inhalt). Es sollte modern und einladend wirken. Wir verwenden im Normalfall den Font "Impact", dies stellt aber kein Killerkriterium dar.

```html
<!DOCTYPE html>
<html lang="de">
<head>
<meta charset="utf-8">
<title>Herbstausstellung – Velo Kranz</title>
<link rel="stylesheet" href="https://fonts.googleapis.com/css2?family=Anton&family=Oswald:wght@500;600;700&display=swap">
<style>
  :root {
    --stage: #2b2b2b;
    --ink-dark: #0d0d0f;
    --brand-red: #e30613;
    --accent-orange: #f5a300;
    --headline-grey: #7c7c7c;
    --white: #ffffff;
    --tagline-ink: #1a1a1a;
  }
  html, body {
    margin: 0;
    padding: 0;
    width: 716px;
    height: 1200px;
    overflow: hidden;
    background: var(--stage);
  }
  .poster {
    position: absolute;
    left: 28px;
    top: 132px;
    width: 660px;
    height: 936px;
    background: var(--ink-dark);
    overflow: hidden;
    font-family: "Oswald", "Arial Narrow", sans-serif;
    color: var(--white);
  }
  .hero-photo {
    position: absolute;
    left: 0; top: 0;
    width: 660px; height: 538px;
    background:
      radial-gradient(ellipse 120px 260px at 320px 270px, #8a8a8a 0%, #4a4a4a 35%, rgba(20,20,22,0) 75%),
      radial-gradient(ellipse 220px 300px at 520px 260px, #2c2c30 0%, #151518 60%, #0b0b0d 100%),
      linear-gradient(180deg, #0a0a0b 0%, #1b1b1e 60%, #2a2a2d 100%);
  }
  .logo-plate {
    position: absolute;
    left: 191px; top: 0;
    width: 267px; height: 72px;
  }
  .logo-plate .wordmark {
    height: 50px;
    background: var(--brand-red);
    display: flex;
    align-items: center;
    justify-content: center;
    font-weight: 700;
    font-size: 32px;
    letter-spacing: 1px;
    text-transform: uppercase;
    color: var(--white);
  }
  .logo-plate .tagline {
    height: 22px;
    background: var(--white);
    color: var(--tagline-ink);
    font-weight: 600;
    font-size: 13px;
    line-height: 22px;
    text-align: center;
    letter-spacing: 0.3px;
  }
  .headline {
    position: absolute;
    left: 0; top: 0;
    width: 660px; height: 936px;
    pointer-events: none;
  }
  .headline text {
    font-family: "Anton", "Impact", sans-serif;
    fill: var(--headline-grey);
    fill-opacity: 0.82;
  }
  .info-panel {
    position: absolute;
    left: 0; top: 538px;
    width: 660px; height: 398px;
    background: var(--brand-red);
  }
  .event-date {
    position: absolute;
    left: 40px; top: 30px;
  }
  .event-date text {
    font-family: "Oswald", "Impact", sans-serif;
    font-weight: 700;
    fill: var(--white);
  }
  .details {
    position: absolute;
    left: 38px;
    top: 0;
    margin: 0;
    font-weight: 600;
    font-size: 19px;
    line-height: 22.6px;
    letter-spacing: -0.2px;
  }
  .details p { margin: 0; position: absolute; white-space: nowrap; }
  .label-wide { letter-spacing: 2.5px; font-weight: 700; }
  .highlight { color: var(--accent-orange); letter-spacing: 1.2px; }
  .brands .brand {
    position: absolute;
    font-weight: 700;
    color: var(--white);
    white-space: nowrap;
  }
  .brand-qrz { left: 482px; top: 292px; font-size: 20px; display: flex; align-items: center; gap: 6px; }
  .brand-qrz .dot { width: 26px; height: 26px; border: 2px solid var(--white); border-radius: 50%; box-sizing: border-box; }
  .brand-fvl { left: 575px; top: 292px; font-size: 20px; }
  .brand-harimo { left: 553px; top: 334px; font-size: 18px; letter-spacing: 0.5px; }
  .web-bar {
    position: absolute;
    left: 197px; top: 371px;
    width: 271px; height: 27px;
    background: var(--white);
    color: var(--brand-red);
    font-weight: 700;
    font-size: 15px;
    line-height: 27px;
    letter-spacing: 3px;
    text-align: center;
  }
</style>
</head>
<body>
  <main class="poster">
    <div class="hero-photo" role="img" aria-label="Dunkles Foto eines Motorradhelms mit hell gemustertem Streifen"></div>

    <div class="logo-plate">
      <div class="wordmark">Velo Kranz</div>
      <div class="tagline">IHR ZWEIRADHAUS im Mittelland</div>
    </div>

    <section class="info-panel">
      <svg class="event-date" width="590" height="54" viewBox="0 0 590 54">
        <text x="0" y="46" font-size="50" textLength="576" lengthAdjust="spacing">20.-22. OKTOBER 2017</text>
      </svg>

      <div class="details">
        <p style="top:90px"><span class="label-wide">ÖFFNUNGSZEITEN</span>&nbsp; Fr. 14 - 19 Uhr · Sa. 8 - 19 Uhr · So. 9 - 16 Uhr</p>
        <p style="top:117px">Saisonausverkauf mit <span class="highlight">-20% AUF MOTORRADBEKLEIDUNG</span></p>
        <p style="top:139px">und Zubehör - nur auf nicht reduzierte Lagerware</p>
        <p style="top:167px"><span class="highlight">NETTOPREISE</span> auf Zubehör &amp; Bekleidung im Schnäppchenzelt</p>
        <p style="top:196px">Unsere <span class="highlight">LIVEMUSIK</span> im Festzelt</p>
        <p style="top:218px">Freitag ab 20 Uhr Vinyl Abend mit Dustrider</p>
        <p style="top:240px">Samstag ab 20 Uhr Festmusik mit Bergklang-Ost</p>
        <p style="top:262px">Sonntag 9 -16 Uhr Matinée</p>
        <p style="top:302px; font-size:17px">Talackerweg 14 · 5040 Steinfeld</p>
        <p style="top:323px; font-size:17px">Tel. 062 410 26 38</p>
      </div>

      <div class="brands">
        <div class="brand brand-qrz"><span class="dot"></span>QRZ</div>
        <div class="brand brand-fvl">FVL</div>
        <div class="brand brand-harimo">HARIMO</div>
      </div>

      <div class="web-bar">www.velo-kranz.ch</div>
    </section>

    <svg class="headline" width="660" height="936" viewBox="0 0 660 936" aria-label="Herbst Ausstellung">
      <text x="0" y="443" font-size="228" textLength="660" lengthAdjust="spacingAndGlyphs">HERBST</text>
      <text x="0" y="538" font-size="134" textLength="660" lengthAdjust="spacingAndGlyphs">AUSSTELLUNG</text>
    </svg>
  </main>
</body>
</html>
```